Clean Energy Brand - Business Card and Letterhead Designs

Hi, everyone! We need a graphic designer who has experience working with the energy sector. We want help designing a perfect two-sided business card and letterhead for a clean energy company we've been assisting. We have a great new logo and all of the associated files.Our client is looking for a design that is "disruptive," "future-facing," "masculine," "bold," and "empowering." The colours of the logo are navy blue and orange and are meant to stand out. We'll need all ownership and copyright paperwork as well as first proofs in a 48-hour period.

Target Market(s)

Government; Non-Profits; Clean Energy Industry; Municipalities; North American Energy Sector

Industry/Entity Type

Power Generation

Requirements
Must have
• A matching business card and letterhead design
Should not have
• Must not be from a template

```html
<!DOCTYPE html>
<html lang="en">
<head>
<meta charset="utf-8">
<title>Northwind Clean Energy – Business Card</title>
<link rel="stylesheet" href="https://fonts.googleapis.com/css2?family=Arimo:wght@400;700&display=swap">
<style>
  :root {
    --backdrop: #b4b5bd;
    --charcoal: #2b2a29;
    --orange: #f45a22;
    --paper: #ffffff;
    --ink: #2b2a29;
    --rule: #c9c9c9;
  }
  * { box-sizing: border-box; margin: 0; padding: 0; }
  html, body {
    width: 1200px; height: 1041px; overflow: hidden;
    background: var(--backdrop);
    font-family: "Arimo", Arial, sans-serif;
  }
  .canvas { position: relative; width: 1200px; height: 1041px; }
  .card { position: absolute; left: 294px; width: 628px; height: 360px; overflow: hidden; }
  .card--front { top: 126px; background: var(--charcoal); }
  .card--back { top: 547px; height: 361px; background: var(--paper); }

  .corner-mark {
    position: absolute; left: -205px; top: -205px;
    width: 410px; height: 410px; border-radius: 50%;
    background: var(--orange);
  }

  .brand-name { font-weight: 700; white-space: nowrap; line-height: 1.05; }
  .card--front .brand-name {
    position: absolute; right: 57px; top: 236px;
    font-size: 36px; color: var(--paper); text-align: right;
  }

  .back-brand {
    position: absolute; left: 0; width: 338px; top: 104px;
    display: flex; flex-direction: column; align-items: center; gap: 12px;
  }
  .brand-dot { width: 50px; height: 50px; border-radius: 50%; background: var(--orange); }
  .card--back .brand-name { font-size: 28px; color: var(--ink); text-align: center; }

  .divider {
    position: absolute; left: 338px; top: 83px; width: 1px; height: 168px;
    background: var(--rule);
  }
  .contact { position: absolute; left: 376px; top: 80px; color: var(--ink); }
  .contact__name { font-size: 20px; font-weight: 700; color: var(--orange); letter-spacing: 0.2px; }
  .contact__role { font-size: 14.5px; margin-top: 2px; }
  .contact__list { list-style: none; margin-top: 14px; }
  .contact__item { display: flex; align-items: center; gap: 7px; font-size: 14.5px; line-height: 21px; }
  .contact__item svg { width: 15px; height: 15px; flex: none; }
  .contact__address { font-size: 14.5px; line-height: 19px; margin-top: 16px; }

  .footer-band { position: absolute; left: 0; bottom: 0; width: 628px; height: 40px; }
</style>
</head>
<body>
<main class="canvas">
  <section class="card card--front" aria-label="Business card front">
    <div class="corner-mark" role="img" aria-label="Brand symbol area"></div>
    <p class="brand-name">Northwind<br>Clean Energy</p>
  </section>

  <section class="card card--back" aria-label="Business card back">
    <div class="back-brand">
      <span class="brand-dot"></span>
      <p class="brand-name">Northwind<br>Clean Energy</p>
    </div>
    <div class="divider"></div>
    <div class="contact">
      <p class="contact__name">SAM KERROW</p>
      <p class="contact__role">General Manager</p>
      <ul class="contact__list">
        <li class="contact__item">
          <svg viewBox="0 0 16 16" aria-hidden="true"><path fill="#f45a22" d="M4 1.5l2.2 2.6-1.3 1.6c.8 2 2.3 3.6 4.3 4.5l1.6-1.3 2.6 2.2-1.2 2.4C7 13.3 2.6 8.9 1.6 2.7z"/></svg>
          555-014-2290
        </li>
        <li class="contact__item">
          <svg viewBox="0 0 16 16" aria-hidden="true"><rect x="1" y="3.5" width="14" height="9" fill="#f45a22"/><path d="M1.5 4l6.5 5 6.5-5" fill="none" stroke="#fff" stroke-width="1.3"/></svg>
          sam@northwindce.com
        </li>
        <li class="contact__item">
          <svg viewBox="0 0 16 16" aria-hidden="true"><g fill="none" stroke="#f45a22" stroke-width="1.2"><circle cx="8" cy="8" r="6.5"/><ellipse cx="8" cy="8" rx="3" ry="6.5"/><path d="M1.5 8h13M2.5 4.8h11M2.5 11.2h11"/></g></svg>
          www.northwindce.com
        </li>
      </ul>
      <p class="contact__address">24B Harlow Street West<br>Fairview, ON - K2P 4L9</p>
    </div>
    <svg class="footer-band" viewBox="0 0 628 40" aria-hidden="true">
      <polygon fill="#2b2a29" points="0,30 628,30 628,40 0,40"/>
      <polygon fill="#2b2a29" points="325,23 628,23 628,30 320,30"/>
      <polygon fill="#f45a22" points="0,15 338,15 345,8 628,8 628,23 325,23 318,30 0,30"/>
    </svg>
  </section>
</main>
</body>
</html>
```